lawncare business

Lawncare business. Definitely need company name( Pellbrookens) and slogan ( When your grass gets tall, give us a call) and of course contact info..I would like a unique logo that is lawncare related and alot of attention getting color on the card.

Industry/Entity Type

Business

Contact Information for Business Card

Owner: Dale Penwick Pellbrookens
(555) 614-2087 When your grass gets tall, give us a call.

Requirements
Must have
• Unique lawncare related logo......company name and slogan.....Contact info

```html
<!DOCTYPE html>
<html lang="en">
<head>
<meta charset="utf-8">
<title>Pellbrookens Lawncare – Business Card</title>
<link rel="stylesheet" href="https://fonts.googleapis.com/css2?family=Fira+Sans:wght@400;600&family=Fira+Sans+Condensed:wght@400;600&family=Roboto:wght@300&display=swap">
<style>
  :root {
    --brand-green: #0f9647;
    --deep-green: #0c6e3d;
    --leaf-green: #b5d67a;
    --paper: #ffffff;
  }
  html, body {
    margin: 0;
    padding: 0;
    overflow: hidden;
    background: var(--paper);
  }
  .card {
    position: relative;
    width: 1200px;
    height: 702px;
    background: var(--paper);
    overflow: hidden;
  }
  .brand-mark {
    position: absolute;
    left: 52px;
    top: 57px;
    width: 125px;
    height: 125px;
    background: var(--brand-green);
  }
  .brand-name,
  .brand-descriptor {
    position: absolute;
    left: 193px;
    margin: 0;
    line-height: 1;
    font-family: "Fira Sans", sans-serif;
    text-transform: uppercase;
    white-space: nowrap;
  }
  .brand-name {
    top: 56px;
    font-size: 76px;
    font-weight: 600;
    letter-spacing: -1px;
    color: var(--brand-green);
  }
  .brand-descriptor {
    top: 126px;
    font-size: 63px;
    font-weight: 400;
    letter-spacing: -0.5px;
    color: var(--leaf-green);
  }
  .person {
    position: absolute;
    left: 0;
    right: 0;
    top: 298px;
    text-align: center;
    padding-left: 28px;
  }
  .person-name {
    margin: 0;
    font-family: "Fira Sans Condensed", sans-serif;
    font-weight: 600;
    font-size: 64px;
    line-height: 1;
    color: var(--deep-green);
  }
  .person-role {
    margin: 6px 0 0;
    font-family: "Fira Sans", sans-serif;
    font-weight: 400;
    font-size: 41px;
    line-height: 1;
    letter-spacing: 1px;
    color: var(--leaf-green);
  }
  .contact-band {
    position: absolute;
    left: 0;
    top: 550px;
    width: 1200px;
    height: 152px;
    background: var(--brand-green);
    color: var(--paper);
    font-family: "Roboto", sans-serif;
    font-weight: 300;
  }
  .slogan {
    position: absolute;
    left: 38px;
    top: 30px;
    margin: 0;
    font-size: 31px;
    line-height: 39px;
  }
  .phone {
    position: absolute;
    left: 651px;
    top: 27px;
    margin: 0;
    font-size: 68px;
    line-height: 1;
    letter-spacing: -0.5px;
  }
</style>
</head>
<body>
  <div class="card">
    <header class="brand">
      <div class="brand-mark" aria-hidden="true"></div>
      <h1 class="brand-name">Pellbrookens</h1>
      <p class="brand-descriptor">Lawncare</p>
    </header>

    <section class="person">
      <h2 class="person-name">Dale Penwick</h2>
      <p class="person-role">Owner</p>
    </section>

    <footer class="contact-band">
      <p class="slogan">When your grass gets tall,<br>give us a call !</p>
      <p class="phone">(555) 614-2087</p>
    </footer>
  </div>
</body>
</html>
```